Brochure for Dog Daycare/Overnight Facility

Looking for a multi page brochure for my dog daycare, overnight care, and grooming facility.

Content to be taken from our current website. Please note our website will be updated so please don't take any design elements from it.

Brochure should be professional yet personable with stock images of dogs playing and having fun.

Please see the attached file with the business card so you can see the blue and green colors that we use to brand ourselves.

Here are the different sections to include for content which can all be found on our website at: www.PawHavenLodge.com

Highlight our three main services: Go to the services tab and pull the content from Daycare, Overnight Care, and Grooming.

Use testimonials throughout found: About us tab, left side of page under 'what our clients say'.

Facility highlights: About us tab, left side under 'Facility'.

What makes us different: About us tab, left side of page.

Include the following Frequently Asked Questions and answers:
What is dog daycare?
How often do dog owners take their dogs to Daycare?
I have an old dog, will he/she enjoy this environment?
Does my dog have to be spayed or neutered?
Do you offer indoor and outdoor play areas?
Can I take a tour?
What qualifications do staff members have?
What sets you apart from your competitors?

Make sure to include: phone number, web address, e-mail address, mailing address.
Updates

Thank you all for your submissions.  We are having a hard time deciding with this project.  Hope to have made a decision in the next day or so.

Target Market(s)

Dog owners would love their pets. Medium to higher income. Ages 25-60.

Industry/Entity Type

Business

Requirements
Must have
• Must have all of the content pulled from our website.

Photos of dogs and dogs playing.

Our contact information.

Nice to have
• I would like a corresponding price sheet that is not part of the brochure but can be slid inside. Our pricing can be found on our website. I can get into more specifics on pricing if you choose to provide this option.
Should not have
• Anything cat related.

Should not be cutesie, must be professional and personable. Displaying trust.

```html
<!DOCTYPE html>
<html lang="en">
<head>
<meta charset="utf-8">
<title>Paw Haven Lodge Brochure and Price Sheet</title>
<link href="https://fonts.googleapis.com/css2?family=Didact+Gothic&family=Questrial&family=Oswald:wght@500&family=Montserrat:wght@700&display=swap" rel="stylesheet">
<style>
:root{
  --green:#a9c43b;
  --green-light:#e7efcd;
  --blue:#b2dfe3;
  --brown:#4a3b27;
  --ink:#3a3128;
  --rule:#bdbdbd;
}
*{margin:0;padding:0;box-sizing:border-box}
html,body{width:1084px;height:1200px;overflow:hidden;background:#fff}
body{position:relative;font-family:"Didact Gothic",sans-serif;color:var(--ink)}
.sheet{position:absolute;background:#fff;border:1px solid var(--rule);overflow:hidden}
.sheet-outside{left:56px;top:41px;width:715px;height:553px}
.sheet-inside{left:56px;top:603px;width:715px;height:553px}
.bands{position:absolute;left:0;top:0;width:100%;height:100%}
.fold{position:absolute;top:0;bottom:0;width:1px;background:#e3e3e3}
.panel{position:absolute}
.faq{font-size:6.1px;line-height:9.7px}
.faq-title{position:absolute;left:20px;top:42px;font-family:"Questrial",sans-serif;font-size:34px;color:var(--green-light);letter-spacing:1px}
.faq-q{font-family:"Oswald",sans-serif;font-weight:500;font-size:6.4px;letter-spacing:.1px;margin-top:5px;color:var(--ink)}
.faq-q:first-child{margin-top:0}
.quotes{font-size:6.2px;line-height:9.6px}
.quote{font-style:italic;margin-bottom:12px}
.quote cite{display:block;margin-top:3px}
.brand{position:absolute;left:491px;top:180px;width:220px;text-align:center;font-family:"Questrial",sans-serif;color:var(--brown)}
.brand-mark{width:64px;height:64px;background:var(--blue);margin:0 auto 6px}
.brand-the{font-size:12px;letter-spacing:2px}
.brand-name{font-size:26px;letter-spacing:1px;line-height:28px}
.contact{position:absolute;font-family:"Questrial",sans-serif;color:#fff;font-size:8.6px;line-height:12px;letter-spacing:.2px;white-space:nowrap}
.cover-the{position:absolute;left:142px;top:8px;font-family:"Questrial",sans-serif;font-size:26px;color:#fff;letter-spacing:2px}
.cover-name{position:absolute;left:14px;top:30px;font-family:"Questrial",sans-serif;font-size:58px;font-weight:400;color:#fff;letter-spacing:2px;line-height:60px}
.tag{position:absolute;height:18px;background:var(--brown);color:#fff;font-family:"Montserrat",sans-serif;font-weight:700;font-size:15px;line-height:18px;padding-left:20px;letter-spacing:.5px}
.body{font-size:6.6px;line-height:9.8px}
.body p{margin-bottom:9.8px}
.why{list-style:none}
.why li{position:relative;padding-left:12px;margin-bottom:4px}
.why li::before{content:"";position:absolute;left:0;top:2px;width:6px;height:6px;border-radius:50%;background:var(--brown)}
.web{position:absolute;font-family:"Questrial",sans-serif;color:#fff;font-size:15px;letter-spacing:.3px;white-space:nowrap}
.sheet-price{left:810px;top:284px;width:228px;height:553px;border-color:#333}
.spine{position:absolute;left:0;top:0;width:54px;height:100%;background:var(--brown)}
.spine-line{position:absolute;left:54px;top:0;width:3px;height:100%;background:var(--blue)}
.vert{position:absolute;transform-origin:left top;transform:rotate(-90deg);font-family:"Questrial",sans-serif;color:var(--blue);white-space:nowrap}
.price-head{position:absolute;left:57px;right:0;background:var(--green);color:#fff;font-family:"Questrial",sans-serif;font-size:18px;text-align:right;padding-right:4px;line-height:20px}
.price-list{position:absolute;left:116px;width:104px;font-size:7.2px;line-height:9px}
.price-list div{display:flex;justify-content:space-between}
.price-list span:last-child{width:20px}
.price-note{position:absolute;left:84px;width:140px;font-size:6px;line-height:7.4px;text-align:center}
</style>
</head>
<body>

<section class="sheet sheet-outside">
  <svg class="bands" viewBox="0 0 715 553" aria-hidden="true">
    <polygon points="0,0 715,0 715,95 0,84" fill="var(--green)"/>
    <polygon points="0,84 715,95 715,103 0,91" fill="var(--green-light)"/>
    <polygon points="238,530 715,512 715,553 238,553" fill="var(--blue)"/>
  </svg>
  <div class="fold" style="left:238px"></div>
  <div class="fold" style="left:477px"></div>

  <h2 class="faq-title">FAQS</h2>

  <div class="panel faq" style="left:12px;top:108px;width:222px">
    <div class="faq-q">WHAT IS DOG DAYCARE?</div>
    <div>Dog daycare is a safe, fun, social play environment for your dog. It works a lot like human daycare in that you can drop your dog off for any number of hours during a day and while here he will be able to play with other dogs, staff members, inside and outside all so that when you come home from a long day at work you aren't greeted by an over-excited, stressed-out dog.</div>
    <div class="faq-q">HOW OFTEN DO DOG OWNERS TAKE THEIR DOGS TO DAYCARE?</div>
    <div>It varies greatly from client to client, we have some guests that visit us daily and others that we only see a couple of times per month. The amount of daycare you feel is necessary for your dog to maintain a healthy and active lifestyle is a decision only you can make.</div>
    <div class="faq-q">I HAVE AN OLD DOG, WILL HE/SHE ENJOY THIS ENVIRONMENT?</div>
    <div>Dogs of every age and activity level have enjoyed all of our services. Our staff members cater to the individual needs of each guest every day to ensure a positive experience during every visit. While your older dog may not run around and play as much as the younger dogs that visit us, he will still appreciate being around other dogs. Socialization, even for an older dog, can be a great part of a healthy and happy lifestyle.</div>
    <div class="faq-q">DOES MY DOG HAVE TO BE SPAYED OR NEUTERED?</div>
    <div>In order to participate in daycare or group play all dogs must be spayed or neutered before the age of 7 months. Unaltered pets are, however, welcome to participate in Overnight Care and Grooming Services.</div>
    <div class="faq-q">DO YOU OFFER INDOOR AND OUTDOOR PLAY AREAS?</div>
    <div>Yes, our facility offers indoor and outdoor play areas for both large and small dogs.</div>
    <div class="faq-q">CAN I TAKE A TOUR?</div>
    <div>Absolutely! Our client services staff members are more than happy to take you on an informative tour through the public areas at any Paw Haven Lodge location and share with you everything Paw Haven Lodge has to offer. Tours are welcome anytime during normal business hours.</div>
    <div class="faq-q">WHAT QUALIFICATIONS DO STAFF MEMBERS HAVE?</div>
    <div>We have a team of very qualified individuals at each Paw Haven Lodge facility. Staff members are certified in Canine First Aid and CPR and are trained in dog behavior and socialization monitoring.</div>
    <div class="faq-q">WHAT SETS YOU APART FROM YOUR COMPETITORS?</div>
    <div>Paw Haven Lodge offers the widest variety of services and amenities dedicated to the health and happiness of each guest. We recognize that each guest has a different personality with different needs, which is why we come highly recommended by leading veterinary clinics throughout the Fox Valley.</div>
  </div>

  <div class="panel quotes" style="left:272px;top:117px;width:196px">
    <p class="quote">"I would recommend Paw Haven Lodge to any and everyone who is looking for a daycare they can trust. Biscuit is not just a pet, he is a part of my family and they treat him as part of theirs as well. This is a five-star facility for my pet and I just want to say thank you to all of the staff for being so loving and caring."<cite>- Dana Whitfield &amp; Mark Olsen, owners of Biscuit</cite></p>
    <p class="quote">"I was thrilled to find Paw Haven Lodge, a place for Clover where she gets the same amount of love and attention that she gets when she's home."<cite>-Renee, owner of Clover</cite></p>
    <p class="quote">"We have had pets for the last 26 years and the quality of service provided by Paw Haven Lodge is among the best I have encountered. My family is confident when we are on vacation the dogs are also on their own vacation enjoying the quality care provided by Paw Haven Lodge."<cite>-Marta K</cite></p>
    <p class="quote">"Paw Haven Lodge is a wonderful facility with a dedicated and caring staff. We use Paw Haven Lodge for training classes, daycare, overnight extended care and grooming. We've been very pleased with their services and the best part is Rocco loves going to Paw Haven Lodge. If he's happy, we are happy."<cite>-Tom and Ellen Brandt, owners of Rocco</cite></p>
    <p class="quote">"You raised the bar standard for pet care."<cite>-Greg and Lisa Novak, owners of Juniper</cite></p>
  </div>

  <div class="brand">
    <div class="brand-mark"></div>
    <div class="brand-the">THE</div>
    <div class="brand-name">PAW HAVEN</div>
  </div>

  <div class="contact" style="left:497px;top:526px">2480 MEADOWBROOK LN<br>LAKEVIEW, WI 54900</div>
  <div class="contact" style="left:624px;top:526px">P: 920-555-0142<br>F: 920-555-0143</div>
</section>

<section class="sheet sheet-inside">
  <svg class="bands" viewBox="0 0 715 553" aria-hidden="true">
    <polygon points="0,0 715,0 715,64 0,92" fill="var(--green)"/>
    <polygon points="0,92 715,64 715,72 0,100" fill="var(--green-light)"/>
    <polygon points="0,516 715,506 715,553 0,553" fill="var(--blue)"/>
  </svg>
  <div class="fold" style="left:238px"></div>
  <div class="fold" style="left:477px"></div>

  <div class="cover-the">THE</div>
  <h1 class="cover-name">PAW HAVEN</h1>

  <div class="tag" style="left:0;top:123px;width:135px">GROOMING</div>
  <div class="tag" style="left:276px;top:126px;width:184px">DAYCARE</div>
  <div class="tag" style="left:535px;top:128px;width:180px;padding-left:10px">OVERNIGHT CARE</div>

  <div class="panel body" style="left:16px;top:154px;width:202px">
    <p>What better way to pamper your pooch than with a special treatment at our full service grooming spa. Every dog deserves the best, which is why our professional dog groomers are ready to cater to their every need. Our high quality full service grooming includes a bath with your choice of shampoo, nail trim, ear cleaning, brush out and haircut if necessary.</p>
    <p>Every grooming service utilizes all natural products, so you can be sure your dog is only getting the best. From teeth cleaning to a quick spritz of detangler or a relaxing pawdicure, every treatment or service is also available a la carte and can be done on their own or as the perfect complement to any other grooming service.</p>
    <p>Prices for grooming services may vary by breed, size or coat condition and are performed by appointment only. Please call today to schedule or ask about any of our fabulous spa services.</p>
    <p>Proof of Rabies vaccination and a completed application packet is required prior to any grooming service.</p>
  </div>

  <div class="panel body" style="left:261px;top:153px;width:206px">
    <p>You work long hours and hate to leave your dog home alone all day. While staying at Paw Haven Lodge your dog will play and socialize in a safe and supervised environment with other dogs of the same size or temperament.</p>
    <p>Socialization is one of the most important aspects of canine development. Daycare is an excellent way for canines to learn these social skills as well as burn off excess energy.</p>
    <p>At Paw Haven Lodge, dogs will have the chance to wrestle, play fetch, run around or even catch an afternoon snooze in the warm summer sun. We plan each and every day to deliver the utmost in socialization, safety and fun. Dogs will participate in play groups determined by each dog's size and play style. Don't forget to sign your pet up for our daily ice-cream social, a big hit among all of our guests.</p>
    <p>The benefits of dog daycare are numerous. Your dog's social skills will increase while learning how to play and interact with others in a safe, fun and appropriate way. Boredom and destructive behaviors caused by lack of physical and mental activity and separation anxiety will decrease. Our indoor play areas are comprised of scratch resistant surfaces and 100% recycled rubber flooring providing a more cushioned playing surface to help prevent achy joints.</p>
    <p>For Safety reasons, bully breeds and unaltered dogs over the age of 6 months are not allowed to participate in Dog Daycare, but may still be eligible to visit us for an overnight stay.</p>
  </div>

  <div class="panel body" style="left:498px;top:164px;width:206px">
    <p>Leaving your pet overnight should not be a stressful time for either of you. Your pet's stay with us should be safe and enjoyable just like being at home.</p>
    <p>Each guest will enjoy a peaceful night's sleep in a private suite and has access to well-maintained outdoor areas with accommodations available for those families with multiple pets.</p>
    <p>For the comfort of each guest the latest flooring and climate control systems are found throughout all indoor play and sleeping areas. And you'll be pleased to know we have veterinarians on call 24 hours a day.</p>
    <p>You know that the more activity and interaction your pet receives the happier and healthier they will be. Activity does not necessarily mean exercise, it could be extra cuddle time, feedings or a trip to the groomer to work on nail trimming or brushing. Either way it is important to provide your dog extra attention and interaction while away from home.</p>
    <p>Why Activities?</p>
    <ul class="why">
      <li>Exercise helps keep dogs agile and mobile</li>
      <li>Dogs need physical and mental stimulation daily to thrive</li>
      <li>Helps channel energy into more productive outlets</li>
      <li>Can help timid dogs build trust and confidence</li>
      <li>Exercise reduces digestive problems</li>
    </ul>
  </div>

  <div class="web" style="left:22px;top:524px">WWW.PAWHAVENLODGE.COM</div>
  <div class="web" style="right:14px;top:524px">INFO@PAWHAVENLODGE.COM</div>
</section>

<section class="sheet sheet-price">
  <div class="spine"></div>
  <div class="spine-line"></div>
  <div class="vert" style="left:14px;top:545px;font-size:12px;letter-spacing:1px">THE</div>
  <div class="vert" style="left:24px;top:545px;font-size:34px;letter-spacing:1px;line-height:32px">PAW HAVEN</div>
  <div class="vert" style="left:16px;top:162px;font-size:30px;letter-spacing:1px;line-height:30px">SERVICES</div>

  <div class="price-head" style="top:71px">DAYCARE</div>
  <div class="price-list" style="top:100px">
    <div><span>HALF DAY...........</span><span>14.50</span></div>
    <div><span>5 HALF DAYS.....</span><span>70</span></div>
    <div><span>10 HALF DAYS...</span><span>135</span></div>
  </div>
  <div class="price-list" style="top:140px">
    <div><span>FULL DAY...........</span><span>19.50</span></div>
    <div><span>5 FULL DAYS......</span><span>95</span></div>
    <div><span>10 FULL DAYS....</span><span>185</span></div>
    <div><span>20 FULL DAYS....</span><span>365</span></div>
  </div>

  <div class="price-head" style="top:190px">OVERNIGHT CARE</div>
  <div class="price-note" style="top:218px">Paw Haven Lodge offers a wide variety of activity and vacation options for accomodate the needs of every dog. Call today to talk to a reservation specialist.</div>

  <div class="price-head" style="top:268px;line-height:21px">GROOMING<br>+ SPA RATES</div>
  <div class="price-list" style="left:88px;width:132px;top:318px">
    <div><span>NAIL TRIM.............................</span><span>14</span></div>
    <div><span>TEETH BRUSHING..................</span><span>4</span></div>
    <div><span>EAR PLUCKING.......................</span><span>10</span></div>
    <div><span>FLEA &amp; TICK TREATMENT...</span><span>10</span></div>
  </div>

  <div class="price-head" style="top:381px">GOURMET TREATS</div>
  <div class="price-list" style="left:99px;width:121px;top:413px">
    <div><span>ICE CREAM SOCIAL...</span><span>1.50</span></div>
    <div><span>MARROW BONE.........</span><span>3</span></div>
    <div><span>SEASONAL FEAST.......</span><span>3.50</span></div>
  </div>
</section>

</body>
</html>
```